Dental Practice Billboard Design

We are a newer dental practice in need of a simple but appealing billboard for our growing dental practice to attract new patients. The practice is owned by husband and wife dentists and is family friendly in a small town in Kentucky. We try to be very friendly and caring to our patients. Would prefer a blue background for the billboard and our tooth logo to be prominent. We are partial to the Patua One font used in the image below but please feel free to tweak it as you deem necessary. The shape of the uppercase D and lowercase g are why we like that font, so fonts with a similarly shaped “D” and “g” would work as well. Please include our phone number (606) 847-3962. Please see our website Harlowfamilydentistry.com for more info on the practice if needed. Thank you! Looking forward to seeing your creation.
Updates

The dimensions will be 12ft x 24ft (3.6576m x 7.3152m). Apologies for not including this in the original prompt. Thank you all for your submissions.

Industry/Entity Type

Dental

Font styles to use
Other font styles liked:
• Patua One

Colors
0054AA
0677BA
7BADD7
CADEEF
E8F1F8
0094D4
00A9DD
6FCCEA
C7EBF8
E9F6FB
00AB8E
00BBA5
67D7C9
C6EFE9
E9F9F6
59FF00
82FF00
B8FF75
E3FFCB
F4FFEA

Requirements
Must have
• Phone number, website, Logo, Practice name “Harlow Family Dentistry”
Should not have
• A tagline or slogan

```html
<!DOCTYPE html>
<html lang="en">
<head>
<meta charset="utf-8">
<title>Harlow Family Dentistry Billboard</title>
<link href="https://fonts.googleapis.com/css2?family=Patua+One&family=Encode+Sans+Semi+Condensed:wght@600&display=swap" rel="stylesheet">
<style>
  :root {
    --navy: #1a2b5a;
    --green: #2bb34b;
    --white: #ffffff;
    --skin-light: #e9c2b0;
    --skin-dark: #b77a66;
  }
  * { margin: 0; padding: 0; box-sizing: border-box; }
  html, body { width: 1200px; height: 625px; overflow: hidden; background: var(--navy); }
  .billboard {
    position: relative;
    width: 1200px;
    height: 625px;
    background: var(--navy);
    overflow: hidden;
    font-family: "Patua One", serif;
  }
  .smile-photo {
    position: absolute;
    left: 810px;
    top: 0;
    width: 390px;
    height: 325px;
    border-top-left-radius: 40px 325px;
    background: radial-gradient(ellipse at 60% 45%, #f2d5c7 0%, var(--skin-light) 45%, var(--skin-dark) 100%);
  }
  .brand-dot {
    position: absolute;
    left: 182px;
    top: 92px;
    width: 110px;
    height: 110px;
    border-radius: 50%;
    background: var(--green);
  }
  .brand {
    position: absolute;
    left: 327px;
    top: 88px;
    color: var(--white);
  }
  .brand-name {
    font-size: 84px;
    line-height: 1;
  }
  .brand-sub {
    font-size: 42px;
    line-height: 1;
    margin-top: 12px;
  }
  .band {
    position: absolute;
    left: 0;
    top: 325px;
    width: 1200px;
    height: 176px;
    background: var(--green);
  }
  .website {
    position: absolute;
    top: 370px;
    width: 100%;
    text-align: center;
    color: var(--white);
    font-size: 43px;
    line-height: 1;
  }
  .phone-pill {
    position: absolute;
    left: 332px;
    top: 444px;
    width: 536px;
    height: 116px;
    border-radius: 58px;
    background: var(--green);
    border: 6px solid var(--navy);
    display: flex;
    align-items: center;
    justify-content: center;
    gap: 12px;
  }
  .phone-icon { width: 40px; height: 60px; }
  .phone-number {
    color: var(--white);
    font-family: "Encode Sans Semi Condensed", sans-serif;
    font-weight: 600;
    font-size: 62px;
    line-height: 1;
  }
</style>
</head>
<body>
  <div class="billboard">
    <div class="smile-photo" role="img" aria-label="Close-up photo of a smiling mouth with white teeth"></div>

    <div class="brand-dot"></div>
    <div class="brand">
      <div class="brand-name">Harlow</div>
      <div class="brand-sub">Family Dentistry</div>
    </div>

    <div class="band"></div>
    <p class="website">Harlowfamilydentistry.com</p>

    <div class="phone-pill">
      <svg class="phone-icon" viewBox="0 0 40 60" aria-hidden="true">
        <path d="M16 2 C22 0 26 4 26 8 L24 16 C23 20 18 20 16 22 C13 30 13 36 17 44 C20 45 24 44 27 47 L31 53 C33 57 28 60 23 59 C12 56 4 44 4 30 C4 16 9 5 16 2 Z" fill="#1a2b5a"/>
      </svg>
      <span class="phone-number">(606) 847-3962</span>
    </div>
  </div>
</body>
</html>
```